Recruiting ad for Caregivers and Nurses

We need a few amazing, fun, catchy, creative recruiting ads for Caregivers and Nurses to care for homecare patients on the island of Oahu, in Hawaii. We are an in home care company called Parkdale Homecare. Our care services are provided 24/7, so we need staff that can work days, nights, weekdays, weekends. We need catchy fun ads to entice caregivers and nurses to call our office to inquire about jobs available. Our patients age range is from babies to seniors. We need caregivers and nurses for basic patient care (bathing, dressing, ambulating, preparing meals, medication reminders, light housekeeping) and complex patients (oxygen, tube feeding, injections, vents, wound care). Here are some bullets to consider including:
*Full-time and Part-time Positions Available (days, nights, weekdays, weekends)
*Sign-On Bonus Programs Offered up to $500
*Refer a Friend Bonus Program
*Holiday Pay
*2 Health Plans to Choose from
*Island-Wide Locations
*All PPE Provided (masks, gloves, etc)
*401K Program
*Tuition Benefits

```html
<!DOCTYPE html>
<html lang="en">
<head>
<meta charset="utf-8">
<title>Parkdale Homecare – Join Our Team</title>
<link href="https://fonts.googleapis.com/css2?family=Cinzel:wght@400;500&family=Source+Sans+3:wght@400;600&display=swap" rel="stylesheet">
<style>
  :root {
    --teal: #1d6a62;
    --salmon: #f0957e;
    --salmon-soft: #f6b19f;
    --rose: #c68676;
    --peach-bg: #fdebe3;
    --text: #4a4544;
    --white: #ffffff;
  }
  * { margin: 0; padding: 0; box-sizing: border-box; }
  html, body { width: 1200px; height: 859px; overflow: hidden; background: var(--white); }
  .ad {
    position: relative;
    width: 1200px; height: 859px; overflow: hidden;
    background: radial-gradient(circle at 20% 18%, #fff8f4 0%, var(--peach-bg) 55%, #f9ddd2 100%);
    font-family: "Source Sans 3", sans-serif;
    color: var(--text);
  }
  .shapes { position: absolute; inset: 0; }
  .headline {
    position: absolute; left: 52px; top: 52px;
    font-family: "Cinzel", serif; font-weight: 400;
    font-size: 68px; line-height: 1; color: var(--teal); letter-spacing: 1px;
  }
  .role-band {
    position: absolute; left: 50px; top: 152px; width: 504px; height: 46px;
    background: var(--salmon); color: var(--white);
    font-size: 35px; font-weight: 400; letter-spacing: 3px;
    display: flex; align-items: center; justify-content: center;
  }
  .benefits {
    position: absolute; left: 58px; top: 232px; list-style: none;
    font-size: 24px; line-height: 1.2;
  }
  .benefits li { position: relative; padding-left: 42px; margin-bottom: 12px; }
  .benefits li svg { position: absolute; left: 0; top: 3px; width: 24px; height: 24px; }
  .benefits .note { display: block; }
  .contact {
    position: absolute; left: 62px; top: 734px; color: var(--white);
    font-size: 22px; line-height: 1.7;
  }
  .contact p { display: flex; align-items: center; gap: 10px; }
  .contact svg { width: 20px; height: 20px; }
  .brand {
    position: absolute; left: 1004px; top: 0; width: 186px; height: 190px;
    background: var(--white); border-radius: 0 0 70px 70px;
    display: flex; flex-direction: column; align-items: center; justify-content: center; gap: 12px;
    font-family: "Source Sans 3", sans-serif; font-weight: 600; color: var(--teal);
    font-size: 30px; line-height: 1.05; text-align: center;
  }
  .brand-dot { width: 34px; height: 34px; border-radius: 50%; background: var(--salmon); }
  .badge { position: absolute; left: 508px; top: 536px; width: 232px; height: 232px; }
  .badge-text {
    position: absolute; inset: 0; display: flex; flex-direction: column;
    align-items: center; justify-content: center; color: var(--white); text-align: center;
  }
  .badge-text .big { font-size: 31px; letter-spacing: 3px; line-height: 1.2; }
  .badge-text .small { font-size: 19px; letter-spacing: 2px; margin-top: 10px; font-weight: 600; }
</style>
</head>
<body>
<main class="ad">
  <svg class="shapes" viewBox="0 0 1200 859" width="1200" height="859">
    <defs>
      <linearGradient id="photoTone" x1="0" y1="0" x2="1" y2="1">
        <stop offset="0" stop-color="#4f6b3a"/>
        <stop offset="0.4" stop-color="#8fc9c4"/>
        <stop offset="0.75" stop-color="#e9c2b0"/>
        <stop offset="1" stop-color="#b9936f"/>
      </linearGradient>
      <linearGradient id="roseBand" x1="0" y1="0" x2="1" y2="0">
        <stop offset="0" stop-color="#b5766a"/>
        <stop offset="1" stop-color="#e7a793"/>
      </linearGradient>
    </defs>
    <path class="photo-area" role="img" aria-label="Photo of a smiling caregiver in a light blue uniform holding hands with an elderly woman outdoors"
          d="M672,0 L1200,0 L1200,859 L610,859 C585,700 590,420 620,250 C635,150 652,70 672,0 Z" fill="url(#photoTone)"/>
    <path d="M666,0 C640,90 616,200 603,330 C590,480 592,680 612,859" fill="none" stroke="var(--rose)" stroke-width="6"/>
    <path d="M0,658 C200,642 460,690 690,859 L0,859 Z" fill="url(#roseBand)"/>
    <path d="M0,690 C220,676 450,725 650,859 L0,859 Z" fill="var(--white)"/>
    <path d="M0,704 C220,692 440,740 622,859 L0,859 Z" fill="var(--salmon)"/>
  </svg>

  <h1 class="headline">Join our team</h1>
  <div class="role-band">CAREGIVERS &amp; NURSES</div>

  <ul class="benefits">
    <li><svg viewBox="0 0 24 24"><circle cx="12" cy="12" r="12" fill="#f0957e"/><path d="M7 12.5l3.2 3L17 8.8" fill="none" stroke="#fff" stroke-width="2.2"/></svg>Full-time and Part-time Positions Available<span class="note">(days, nights, weekdays, weekends)</span></li>
    <li><svg viewBox="0 0 24 24"><circle cx="12" cy="12" r="12" fill="#f0957e"/><path d="M7 12.5l3.2 3L17 8.8" fill="none" stroke="#fff" stroke-width="2.2"/></svg>Sign-On Bonus Programs Offered up to $500</li>
    <li><svg viewBox="0 0 24 24"><circle cx="12" cy="12" r="12" fill="#f0957e"/><path d="M7 12.5l3.2 3L17 8.8" fill="none" stroke="#fff" stroke-width="2.2"/></svg>Refer a Friend Bonus Program</li>
    <li><svg viewBox="0 0 24 24"><circle cx="12" cy="12" r="12" fill="#f0957e"/><path d="M7 12.5l3.2 3L17 8.8" fill="none" stroke="#fff" stroke-width="2.2"/></svg>Holiday Pay</li>
    <li><svg viewBox="0 0 24 24"><circle cx="12" cy="12" r="12" fill="#f0957e"/><path d="M7 12.5l3.2 3L17 8.8" fill="none" stroke="#fff" stroke-width="2.2"/></svg>2 Health Plans to Choose from</li>
    <li><svg viewBox="0 0 24 24"><circle cx="12" cy="12" r="12" fill="#f0957e"/><path d="M7 12.5l3.2 3L17 8.8" fill="none" stroke="#fff" stroke-width="2.2"/></svg>Island-Wide Locations</li>
    <li><svg viewBox="0 0 24 24"><circle cx="12" cy="12" r="12" fill="#f0957e"/><path d="M7 12.5l3.2 3L17 8.8" fill="none" stroke="#fff" stroke-width="2.2"/></svg>All PPE Provided (masks, gloves, etc)</li>
    <li><svg viewBox="0 0 24 24"><circle cx="12" cy="12" r="12" fill="#f0957e"/><path d="M7 12.5l3.2 3L17 8.8" fill="none" stroke="#fff" stroke-width="2.2"/></svg>401K Program</li>
    <li><svg viewBox="0 0 24 24"><circle cx="12" cy="12" r="12" fill="#f0957e"/><path d="M7 12.5l3.2 3L17 8.8" fill="none" stroke="#fff" stroke-width="2.2"/></svg>Tuition Benefits</li>
  </ul>

  <div class="contact">
    <p>Inquire within</p>
    <p><svg viewBox="0 0 20 20"><circle cx="10" cy="10" r="10" fill="#fff"/><path d="M6.5 5.5l2 .2.8 2.3-1.2 1a6 6 0 003 3l1-1.2 2.3.8.2 2c-4.5.8-9-3.7-8.1-8.1z" fill="#f0957e"/></svg>808-555-0142</p>
    <p><svg viewBox="0 0 20 20"><circle cx="10" cy="10" r="10" fill="#fff"/><g fill="none" stroke="#f0957e" stroke-width="1.3"><circle cx="10" cy="10" r="6"/><ellipse cx="10" cy="10" rx="2.6" ry="6"/><path d="M4 10h12"/></g></svg>www.parkdalecare.com</p>
  </div>

  <div class="brand">
    <span class="brand-dot"></span>
    <span>Parkdale<br>Homecare</span>
  </div>

  <div class="badge">
    <svg viewBox="0 0 232 232" width="232" height="232">
      <g fill="var(--teal)">
        <circle cx="116" cy="116" r="100"/>
        <circle cx="116" cy="14" r="14"/><circle cx="142.4" cy="17.5" r="14"/><circle cx="167" cy="27.7" r="14"/><circle cx="188.1" cy="43.9" r="14"/>
        <circle cx="204.3" cy="65" r="14"/><circle cx="214.5" cy="89.6" r="14"/><circle cx="218" cy="116" r="14"/><circle cx="214.5" cy="142.4" r="14"/>
        <circle cx="204.3" cy="167" r="14"/><circle cx="188.1" cy="188.1" r="14"/><circle cx="167" cy="204.3" r="14"/><circle cx="142.4" cy="214.5" r="14"/>
        <circle cx="116" cy="218" r="14"/><circle cx="89.6" cy="214.5" r="14"/><circle cx="65" cy="204.3" r="14"/><circle cx="43.9" cy="188.1" r="14"/>
        <circle cx="27.7" cy="167" r="14"/><circle cx="17.5" cy="142.4" r="14"/><circle cx="14" cy="116" r="14"/><circle cx="17.5" cy="89.6" r="14"/>
        <circle cx="27.7" cy="65" r="14"/><circle cx="43.9" cy="43.9" r="14"/><circle cx="65" cy="27.7" r="14"/><circle cx="89.6" cy="17.5" r="14"/>
      </g>
    </svg>
    <div class="badge-text">
      <span class="big">WE’RE</span>
      <span class="big">RECRUITING</span>
      <span class="small">APPLY NOW</span>
    </div>
  </div>
</main>
</body>
</html>
```